truck and trailer business Wrap Design

needing a redisgn of our truck and trailer wraps, i have attached the current trailer wrap design and pictures of the new trailer needing a wrap design. trailer is 26ft v nose. 8.5 wide and 7.5ft tall need the trucks that pull the trailers to match. 2018 q-380 long bed. i have attached pictures of the truck. 2009 ZEMO 26 FT BOX

Industry/Entity Type

Insulation

Colors

Designer to choose colors to be used in the design.

Requirements
Must have
• wrap needs to be unique and stand out like our current wrap

```html
<!DOCTYPE html>
<html lang="en">
<head>
<meta charset="utf-8">
<title>Summit Spray Foam – Trailer Wrap</title>
<link href="https://fonts.googleapis.com/css2?family=Roboto+Condensed:wght@700&display=swap" rel="stylesheet">
<style>
  :root {
    --page: #e9ecef;
    --wrap-black: #111214;
    --sky-blue: #1ea3e6;
    --bright-blue: #1b8fdc;
    --deep-blue: #2a3fb8;
    --ring-blue: #1a7fd0;
    --white: #ffffff;
    --ink: #0c1420;
    --photo-wood: #c9a57a;
    --photo-wall: #e9e3d6;
  }
  html, body {
    margin: 0;
    width: 1200px;
    height: 900px;
    overflow: hidden;
    background: var(--page);
  }
  .canvas {
    position: relative;
    width: 1200px;
    height: 900px;
  }
  .trailer-wrap {
    position: absolute;
    left: 90px;
    top: 285px;
    width: 1020px;
    height: 330px;
  }
  .wrap-text { font-family: "Roboto Condensed", "Arial Narrow", sans-serif; font-weight: 700; }
  .brand-name { fill: var(--white); font-size: 40px; letter-spacing: 1px; }
  .web-address { fill: var(--sky-blue); font-size: 20px; }
  .service-item { fill: var(--white); font-size: 18px; letter-spacing: .3px; }
  .phone-number { fill: var(--ink); font-size: 28px; }
  .fine-print { fill: var(--ink); font-size: 5px; }
</style>
</head>
<body>
<main class="canvas">
  <svg class="trailer-wrap" viewBox="0 0 1020 330" aria-label="Summit Spray Foam trailer wrap">
    <defs>
      <linearGradient id="lower-band" x1="0" y1="0" x2="1" y2="0">
        <stop offset="0" stop-color="var(--sky-blue)"/>
        <stop offset="0.55" stop-color="var(--bright-blue)"/>
        <stop offset="1" stop-color="var(--deep-blue)"/>
      </linearGradient>
      <linearGradient id="photo-attic" x1="0" y1="0" x2="1" y2="1">
        <stop offset="0" stop-color="var(--photo-wood)"/>
        <stop offset="0.6" stop-color="var(--photo-wall)"/>
        <stop offset="1" stop-color="#9c8f80"/>
      </linearGradient>
      <linearGradient id="photo-framing" x1="0" y1="0" x2="1" y2="1">
        <stop offset="0" stop-color="#d9b98c"/>
        <stop offset="1" stop-color="#8a6a48"/>
      </linearGradient>
    </defs>

    <rect class="wrap-base" width="1020" height="330" fill="var(--wrap-black)"/>

    <path class="swoosh-stripe" fill="var(--sky-blue)"
          d="M0 178 C180 166 380 186 560 218 C740 250 900 272 1020 262 L1020 278 C880 290 720 266 540 234 C360 204 180 190 0 198 Z"/>
    <path class="lower-band" fill="url(#lower-band)"
          d="M0 210 C180 202 380 220 540 250 C720 284 880 304 1020 292 L1020 330 L0 330 Z"/>

    <g class="photo-ring">
      <circle cx="870" cy="148" r="135" fill="none" stroke="var(--ring-blue)" stroke-width="3"/>
      <circle cx="870" cy="148" r="125" fill="url(#photo-attic)" stroke="var(--white)" stroke-width="3"
              role="img" aria-label="Photo of an attic with spray foam insulation applied to the walls"/>
    </g>
    <g class="photo-ring">
      <circle cx="700" cy="133" r="92" fill="none" stroke="var(--ring-blue)" stroke-width="3"/>
      <circle cx="700" cy="133" r="82" fill="url(#photo-framing)" stroke="var(--white)" stroke-width="3"
              role="img" aria-label="Photo of an installer in protective gear spraying foam into wall framing"/>
    </g>

    <line class="brand-rule" x1="35" y1="38" x2="435" y2="38" stroke="var(--white)" stroke-width="2"/>
    <text class="wrap-text brand-name" x="35" y="86">SUMMIT SPRAY FOAM</text>
    <line class="brand-rule" x1="35" y1="103" x2="435" y2="103" stroke="var(--white)" stroke-width="2"/>
    <text class="wrap-text web-address" x="70" y="135">SUMMITSPRAYFOAM.NET</text>

    <g class="service-list">
      <circle cx="443" cy="109" r="3.5" fill="var(--sky-blue)"/>
      <text class="wrap-text service-item" x="455" y="115">SPRAY FOAM</text>
      <circle cx="443" cy="135" r="3.5" fill="var(--sky-blue)"/>
      <text class="wrap-text service-item" x="455" y="141">FIBERGLASS</text>
      <circle cx="443" cy="160" r="3.5" fill="var(--sky-blue)"/>
      <text class="wrap-text service-item" x="455" y="166">INSULATION</text>
      <circle cx="443" cy="185" r="3.5" fill="var(--sky-blue)"/>
      <text class="wrap-text service-item" x="455" y="191">ROOFING</text>
    </g>

    <text class="wrap-text phone-number" x="30" y="265">555-014-2738</text>
    <rect x="30" y="272" width="4" height="4" fill="var(--ink)"/>
    <text class="wrap-text fine-print" x="37" y="276">@summitsprayfoam</text>
    <text class="wrap-text fine-print" x="150" y="276">the premier insulation company</text>
  </svg>
</main>
</body>
</html>
```